RM Cargoline businesscard project

RM Cargoline Ltd is a freshly founded small (3 employees), young (average age is 30 years) company, living from the road transportation market without own tools.
We would like to have an impressive, new-line, cool busines card for a freshly founded forwarding company on an overcrowded market which raises attention and makes the potential partners eager to work with us.

Target Market(s)

The main profile of the company is logistic/forwarding on road.

Industry/Entity Type

Freight Forwarding

Contact Information for Business Card

Name: Berki Zsófia
Title: general manager
mobile nr: +36-70/482-5193
fax nr: +36-1/534-9061
e-mail: zsofia.berki@rmcargoline.example
info@rmcargoline.example
website address: http://www.rmcargoline.example
and if possible maybe some funny or helpful info on the back

Requirements
Must have
• contact details above
Nice to have
• some really nice and catching back-side (info, graphics, useful tool info... anything)
Should not have
• trucks, road, ship, airplane on it...

```html
<!DOCTYPE html>
<html lang="en">
<head>
<meta charset="utf-8">
<title>RM Cargoline – Business Card, Front and Back</title>
<link rel="stylesheet" href="https://fonts.googleapis.com/css2?family=Questrial&display=swap">
<style>
  :root {
    --page-bg: #e9e7e3;
    --card-white: #f7f7f7;
    --card-dark: #2f3033;
    --card-dark-deep: #232427;
    --accent-blue: #5f8fc6;
    --accent-blue-deep: #4873a8;
    --ink-dark: #2b2b2b;
    --ink-light: #f2f2f2;
    --ink-muted: #c9ccd2;
  }
  * { margin: 0; padding: 0; box-sizing: border-box; }
  html, body {
    width: 1200px; height: 1023px; overflow: hidden;
    background: var(--page-bg);
    font-family: "Questrial", "Century Gothic", sans-serif;
  }
  .card {
    position: absolute; left: 250px;
    width: 700px; height: 400px;
    box-shadow: 0 12px 34px rgba(0,0,0,.2);
    overflow: hidden;
  }
  .card-front { top: 70px; background: var(--card-white); }
  .card-back { top: 553px; background: var(--card-dark); }
  .card-shapes { position: absolute; inset: 0; }

  .brand {
    position: absolute; left: 70px; top: 104px;
    display: flex; align-items: center; gap: 18px;
  }
  .brand-square { width: 40px; height: 40px; background: var(--accent-blue); }
  .brand-name { font-size: 36px; line-height: 1; color: var(--ink-dark); letter-spacing: -0.5px; }

  .person {
    position: absolute; right: 34px; top: 226px;
    text-align: right; color: var(--ink-light);
  }
  .person-name { font-size: 24px; line-height: 1.1; }
  .person-title { font-size: 11px; color: var(--ink-muted); margin-top: 2px; }

  .website {
    position: absolute; left: 470px; top: 296px; width: 230px; height: 30px;
    display: flex; align-items: center; gap: 8px; padding-left: 10px;
    color: var(--ink-light); font-size: 11px; letter-spacing: 2px; white-space: nowrap;
  }

  .contacts {
    position: absolute; left: 56px; top: 254px;
    color: var(--ink-light); list-style: none;
  }
  .contacts li { display: flex; align-items: center; gap: 14px; margin-bottom: 8px; }
  .contacts .icon { width: 18px; height: 18px; flex: none; }
  .contacts .lines { display: flex; flex-direction: column; line-height: 1.3; }
  .phone { font-size: 21px; line-height: 1.15; }
  .email { font-size: 13px; }
</style>
</head>
<body>
<article class="card card-front">
  <svg class="card-shapes" width="700" height="400" viewBox="0 0 700 400" aria-hidden="true">
    <defs>
      <linearGradient id="darkPanel" x1="0" y1="0" x2="1" y2="1">
        <stop offset="0" stop-color="#3a3b3f"/>
        <stop offset="1" stop-color="#232427"/>
      </linearGradient>
    </defs>
    <polygon points="0,200 318,200 350,236 0,236" fill="var(--accent-blue)"/>
    <polygon points="0,236 350,236 392,206 700,190 700,400 0,400" fill="url(#darkPanel)"/>
    <polygon points="676,203 700,190 700,214" fill="var(--accent-blue-deep)"/>
    <polygon points="482,296 700,296 700,326 460,326" fill="var(--accent-blue)"/>
  </svg>

  <div class="brand">
    <span class="brand-square"></span>
    <span class="brand-name">RM Cargoline</span>
  </div>

  <div class="person">
    <div class="person-name">Berki Zsófia</div>
    <div class="person-title">General Manager</div>
  </div>

  <div class="website">
    <svg width="14" height="14" viewBox="0 0 20 20" aria-hidden="true">
      <circle cx="10" cy="10" r="8" fill="none" stroke="currentColor" stroke-width="1.6"/>
      <ellipse cx="10" cy="10" rx="3.5" ry="8" fill="none" stroke="currentColor" stroke-width="1.4"/>
      <line x1="2" y1="10" x2="18" y2="10" stroke="currentColor" stroke-width="1.4"/>
    </svg>
    <span>www.rmcargoline.example</span>
  </div>

  <ul class="contacts">
    <li>
      <svg class="icon" viewBox="0 0 24 24" aria-hidden="true">
        <path d="M6 3 l3 0 l1.5 4.5 l-2 1.5 a12 12 0 0 0 6.5 6.5 l1.5 -2 l4.5 1.5 l0 3 a2 2 0 0 1 -2 2 A17 17 0 0 1 4 5 a2 2 0 0 1 2 -2z" fill="currentColor"/>
      </svg>
      <span class="phone">+36-70/482-5193</span>
    </li>
    <li>
      <svg class="icon" viewBox="0 0 24 24" aria-hidden="true">
        <rect x="6" y="3" width="12" height="6" fill="currentColor"/>
        <rect x="3" y="9" width="18" height="8" rx="1" fill="currentColor"/>
        <rect x="6" y="14" width="12" height="7" fill="var(--card-dark)" stroke="currentColor" stroke-width="1.5"/>
      </svg>
      <span class="phone">+36-1/534-9061</span>
    </li>
    <li>
      <svg class="icon" viewBox="0 0 24 24" aria-hidden="true">
        <rect x="2.5" y="5" width="19" height="14" fill="none" stroke="currentColor" stroke-width="1.5"/>
        <path d="M2.5 5 L12 13 L21.5 5 M2.5 19 L9.5 11 M21.5 19 L14.5 11" fill="none" stroke="currentColor" stroke-width="1.5"/>
      </svg>
      <span class="lines">
        <span class="email">info@rmcargoline.example</span>
        <span class="email">zsofia.berki@rmcargoline.example</span>
      </span>
    </li>
  </ul>
</article>

<article class="card card-back">
  <svg class="card-shapes" width="700" height="400" viewBox="0 0 700 400" aria-hidden="true">
    <defs>
      <linearGradient id="backPanel" x1="0" y1="0" x2="1" y2="1">
        <stop offset="0" stop-color="#3a3b3f"/>
        <stop offset="1" stop-color="#232427"/>
      </linearGradient>
    </defs>
    <rect width="700" height="400" fill="url(#backPanel)"/>
    <polygon points="0,0 150,0 0,190" fill="var(--card-dark-deep)"/>
    <polygon points="150,0 196,0 0,250 0,190" fill="var(--accent-blue)"/>
    <polygon points="700,400 550,400 700,210" fill="var(--card-dark-deep)"/>
    <polygon points="550,400 504,400 700,150 700,210" fill="var(--accent-blue)"/>
  </svg>
</article>
</body>
</html>
```